Silver Heron Construction Services

Create a business card for my business consulting company
Danielle Vesk, Founder and CEO
4816 Alder Brook Way, Ste 100
Denver, CO. 80451
303.782.4190 cell
dvesk@silverheronconst.example
www.silverheronconst.example

Target Market(s)

Private Equity and Construction Companies

Industry/Entity Type

Business / Sales Consulting

Contact Information for Business Card

Tag Line that says "Where The Road To Success Is Always Under Construction"

Requirements
Must have
• Logo on both sides of the card.
Nice to have
• Add tagline to the same side of the card as my name and contact info

```html
<!DOCTYPE html>
<html lang="en">
<head>
<meta charset="utf-8">
<title>Silver Heron Construction Services – Business Card</title>
<link rel="stylesheet" href="https://fonts.googleapis.com/css2?family=Poppins:wght@400;500;600;700&display=swap">
<style>
  :root {
    --backdrop: #1d1d1d;
    --ink: #0a0a0a;
    --card-black: #050505;
    --card-black-sheen: #2a2a2a;
    --paper-light: #eeeff1;
    --paper-mid: #c9cbce;
    --white: #ffffff;
    --text-dark: #141414;
  }
  * { box-sizing: border-box; margin: 0; padding: 0; }
  html, body {
    width: 1200px; height: 800px; overflow: hidden;
    background: var(--backdrop);
    font-family: "Poppins", sans-serif;
  }
  .canvas {
    position: relative; width: 1200px; height: 800px;
    display: flex; flex-direction: column; align-items: center; justify-content: center; gap: 40px;
  }
  .card {
    position: relative; width: 600px; height: 343px; overflow: hidden;
    box-shadow: 0 14px 30px rgba(0,0,0,.45);
  }

  /* Front side */
  .card--front {
    background:
      radial-gradient(ellipse 60% 120% at 20% 90%, var(--card-black-sheen) 0%, transparent 60%),
      radial-gradient(ellipse 40% 90% at 75% 10%, #1a1a1a 0%, transparent 65%),
      var(--card-black);
    display: flex; flex-direction: column; align-items: center; justify-content: center;
    color: var(--white);
  }
  .brand {
    display: flex; align-items: center; gap: 12px;
  }
  .brand__mark {
    width: 18px; height: 18px; border-radius: 50%; flex: none;
  }
  .brand__name {
    font-weight: 700; text-transform: uppercase; letter-spacing: .5px; line-height: 1.15;
  }
  .card--front .brand__mark { background: var(--white); }
  .card--front .brand__name { font-size: 26px; max-width: 300px; color: var(--white); }
  .front__tagline {
    margin-top: 44px; text-align: center;
    font-size: 22px; font-weight: 600; line-height: 1.3;
  }
  .front__rule {
    width: 120px; height: 4px; border-radius: 2px; background: var(--white); margin-top: 12px;
  }

  /* Back side */
  .card--back {
    background:
      linear-gradient(120deg, var(--paper-light) 0%, var(--paper-mid) 45%, var(--paper-light) 75%, var(--paper-mid) 100%);
    color: var(--text-dark);
  }
  .card--back .brand {
    position: absolute; top: 38px; right: 40px;
  }
  .card--back .brand__mark { background: var(--ink); width: 14px; height: 14px; }
  .card--back .brand__name { font-size: 20px; max-width: 220px; color: var(--ink); text-align: right; }
  .contact {
    position: absolute; left: 46px; top: 104px;
  }
  .contact__name {
    font-size: 30px; font-weight: 700; text-transform: uppercase; line-height: 1.1;
  }
  .contact__role {
    font-size: 15px; font-weight: 500; text-transform: uppercase; margin-top: 2px;
  }
  .contact__rule {
    width: 140px; height: 3px; background: var(--ink); margin: 6px 0 12px;
  }
  .contact__list { list-style: none; }
  .contact__item {
    display: flex; align-items: flex-start; gap: 10px;
    font-size: 14px; line-height: 1.35; margin-bottom: 5px;
  }
  .contact__icon {
    width: 18px; height: 18px; flex: none; border-radius: 4px; background: var(--ink);
    display: flex; align-items: center; justify-content: center; margin-top: 1px;
  }
  .back__band {
    position: absolute; left: 0; right: 0; bottom: 0; height: 66px;
    background: var(--ink); color: var(--white);
    display: flex; align-items: center; justify-content: center;
    font-size: 17px; font-weight: 700; text-transform: uppercase; letter-spacing: .3px;
  }
</style>
</head>
<body>
<main class="canvas">

  <section class="card card--front" aria-label="Card front">
    <div class="brand">
      <span class="brand__mark"></span>
      <span class="brand__name">Silver Heron Construction Services</span>
    </div>
    <p class="front__tagline">The Road To Success Is Always<br>Under Construction</p>
    <div class="front__rule"></div>
  </section>

  <section class="card card--back" aria-label="Card back">
    <div class="brand">
      <span class="brand__name">Silver Heron Construction Services</span>
      <span class="brand__mark"></span>
    </div>

    <div class="contact">
      <h1 class="contact__name">Danielle Vesk</h1>
      <p class="contact__role">Founder and CEO</p>
      <div class="contact__rule"></div>
      <ul class="contact__list">
        <li class="contact__item">
          <span class="contact__icon">
            <svg width="11" height="11" viewBox="0 0 24 24"><path fill="#fff" d="M6.6 10.8a15.1 15.1 0 0 0 6.6 6.6l2.2-2.2c.3-.3.7-.4 1-.2 1.1.4 2.3.6 3.6.6.6 0 1 .4 1 1V20c0 .6-.4 1-1 1A17 17 0 0 1 3 4c0-.6.4-1 1-1h3.5c.6 0 1 .4 1 1 0 1.3.2 2.5.6 3.6.1.3 0 .7-.2 1z"/></svg>
          </span>
          <span>303.782.4190</span>
        </li>
        <li class="contact__item">
          <span class="contact__icon">
            <svg width="11" height="11" viewBox="0 0 24 24"><path fill="none" stroke="#fff" stroke-width="2.4" d="M3 6h18v12H3zM3 6l9 7 9-7"/></svg>
          </span>
          <span>dvesk@silverheronconst.example</span>
        </li>
        <li class="contact__item">
          <span class="contact__icon">
            <svg width="11" height="11" viewBox="0 0 24 24"><path fill="#fff" d="M12 2a7 7 0 0 0-7 7c0 5 7 13 7 13s7-8 7-13a7 7 0 0 0-7-7zm0 9.5A2.5 2.5 0 1 1 12 6.5a2.5 2.5 0 0 1 0 5z"/></svg>
          </span>
          <span>4816 Alder Brook Way, Ste 100<br>Denver, CO. 80451</span>
        </li>
      </ul>
    </div>

    <div class="back__band">The Road To Success Is Always Under Construction</div>
  </section>

</main>
</body>
</html>
```